Landing Page for an INNOVATIVE Quilt Cover, with "how it works" section

Before I describe what I would like, you need to understand these:

1) This is a marketing page. The PRIMARY OBJECTIVE is to collect email addresses.
2) The target audience is 35 year old stay-at-home mums. Appeal to them (so don't throw in gadgets in your design!)
3) Make the design as SIMPLE and CLEAR as you can.

Alright, let's begin!

I've created a company called "Quollin", and a product called "Snug-Fit Wrap". Quollin is just a name, but the product is what I NEED to visually explain to the target audience.

Very very briefly, the Snug-Fit Wrap opens on 3 sides, and are bound together by velcro. The primary purpose - is to put a smile on the face of a 35 year old mum every time she changes the quilt cover...

In other words, it makes the chore of changing the cover PAINLESS.

The Snug-Fit Wrap also has strategically placed velcro pieces on the underside (refer attached picture). These velcro pieces hold the quilt in place once it's in the cover. You know how sometimes you have a ball of quilt trapped at the bottom of your cover after using it for a couple of weeks? This gets rid of that problem.

So now on to the design...

1) This needs to be a simple, one-page design (in case it's not clear enough!)

2) As I said, the primary objective of this site is to collect email addresses. Therefore, please incorporate a 'form' within your design.

I only need email addresses (i.e. no need for a separate box for names, country etc) but please allow for social plugins (plain square, plain square and Email).

These are some sites you can get inspiration from in terms of the general layout (and simplicity) I want:
- http://brimfolio.com/
- http://www.parvonix.com/
- http://www.ambertwigkit.com/
- http://vintrel.ws/

3) I need you to design a "How It Works" section, which CLEARLY describes how the Snug-Fit Wrap works.

This is my current site: www.quollin.com, It's an e-commerce store which will be disabled soon, but the homepage should give you a good idea of how the Snug-Fit Wrap works (PLEASE NOTE: I DISLIKE my current design as it's still slightly confusing and boorrrriing).

IMPORTANT - It is not critical to show "what's in the box".

These are some sites which may give you an idea of how to design the "how it works" section:
- http://www.pembrook.com/purse/how-it-works.html
- http://www.lantoloan.com/How-LantoLoan-Works-sp-1.html

4) It's OK to raise their curiosity, but as long as your design explains enough of how the product works.

Make it fun.

Remember, I am after those email addresses.

To all designers working on this project:

Part of this job is to re-design the "how it works" section.  Please DO NOT retain the same design you see on www.quollin.com (or merely re-arrange what I already have on quollin.com).

If you have done that, it is likely you will not be picked.

Thanks, and good luck!

Hi All, 

I have updated a raw vector file of my previous design.  This was one of the earlier drafts, so please feel free to edit it.

PLEASE NOTE - as I indicated in my brief, I'm looking for new ideas for this "how-it-works" section, as I dislike this current design.

Thanks

Target Market(s)

30-40 year old, stay at home mums.

Industry/Entity Type

E-Commerce

Requirements
Must have
• - Name of company and product i.e. Quollin Snug-Fit Wrap
- A tagline under the company name and product. For now, go with "Never Struggle To Change Your Quilt Cover Again"

- Have this other tagline somewhere (this is optional):
"We will change the way you use your quilt cover...forever"
Should not have
• nothing is prohibited. Go crazy!

```html
<!DOCTYPE html>
<html lang="en">
<head>
<meta charset="utf-8">
<title>Quollin Snug-Fit Wrap</title>
<link rel="stylesheet" href="https://fonts.googleapis.com/css2?family=Ubuntu:wght@400;700&family=Sorts+Mill+Goudy:ital@0;1&family=Arimo&display=swap">
<style>
  :root {
    --ink: #1c1c1c;
    --body-text: #3a3a3a;
    --muted: #9a9a9a;
    --green: #5b8c3a;
    --green-dark: #2f6b1e;
    --orange: #f47b20;
    --rule: #d6d6d6;
    --ring: #e9e9e9;
    --ring-fill: #f6f6f6;
    --arrow: #cfcfcf;
    --aqua: #45b8d8;
    --aqua-light: #a9e1ee;
    --navy: #1f6fa8;
    --paper: #ffffff;
    --button: #2b2b2b;
  }
  * { box-sizing: border-box; margin: 0; padding: 0; }
  html, body { width: 871px; height: 1200px; overflow: hidden; background: var(--paper); }
  .page { position: relative; width: 871px; height: 1200px; overflow: hidden; font-family: "Ubuntu", sans-serif; color: var(--ink); }

  .swoosh { position: absolute; left: 0; top: 0; width: 871px; height: 160px; }

  .brand { position: absolute; top: 90px; left: 0; width: 871px; text-align: center;
    font-family: "Ubuntu", sans-serif; font-weight: 700; font-size: 146px; line-height: 160px;
    letter-spacing: -4px; color: var(--ink); }

  .tagline { position: absolute; top: 257px; left: 0; width: 871px; text-align: center;
    font-family: "Sorts Mill Goudy", serif; font-size: 28px; color: var(--ink); }

  .intro { position: absolute; top: 307px; left: 58px; width: 772px;
    font-size: 11.6px; line-height: 16px; color: var(--body-text); }

  .section-title { position: absolute; top: 392px; left: 0; width: 871px; text-align: center;
    font-family: "Sorts Mill Goudy", serif; font-size: 31px; color: var(--green); }

  .cycle { position: absolute; left: 0; top: 440px; width: 871px; height: 490px; }

  .step-art { position: absolute; border-radius: 14px; }
  .step-art.open { left: 418px; top: 458px; width: 100px; height: 112px;
    background: linear-gradient(150deg, var(--aqua-light), var(--aqua)); }
  .step-art.fasten { left: 520px; top: 562px; width: 152px; height: 126px;
    background: linear-gradient(150deg, var(--aqua-light), var(--navy)); }
  .step-art.secure { left: 488px; top: 768px; width: 190px; height: 76px;
    background: linear-gradient(160deg, #dff3f8, var(--aqua-light)); }
  .step-art.enjoy { left: 228px; top: 760px; width: 182px; height: 104px;
    background: linear-gradient(150deg, var(--aqua-light), var(--navy)); }
  .step-art.attach { left: 208px; top: 576px; width: 114px; height: 108px;
    background: linear-gradient(150deg, #4a8fcf, var(--navy)); }

  .step-label { position: absolute; font-family: "Arimo", sans-serif; font-size: 15px; line-height: 16px; color: #555; white-space: nowrap; }
  .step-label.right { text-align: right; }
  .badge { display: inline-block; width: 22px; height: 22px; border-radius: 50%;
    background: var(--orange); color: #fff; font-size: 13px; line-height: 22px; text-align: center;
    vertical-align: middle; }
  .label-open { left: 230px; top: 465px; width: 156px; }
  .badge-open { position: absolute; left: 389px; top: 470px; }
  .label-fasten { left: 680px; top: 596px; }
  .label-secure { left: 591px; top: 851px; }
  .label-enjoy { left: 319px; top: 871px; }
  .label-attach { left: 56px; top: 659px; width: 118px; }
  .badge-attach { position: absolute; left: 178px; top: 664px; }

  .rule { position: absolute; left: 53px; width: 780px; height: 1px; background: var(--rule); }
  .rule.top { top: 932px; }
  .rule.bottom { top: 1161px; }

  .signup-title { position: absolute; top: 952px; left: 0; width: 871px; text-align: center;
    font-family: "Sorts Mill Goudy", serif; font-size: 24px; color: var(--ink); }
  .signup-title em { font-style: normal; color: var(--green-dark); }
  .signup-note { position: absolute; top: 992px; left: 0; width: 871px; text-align: center;
    font-size: 16px; line-height: 22px; color: var(--ink); }

  .signup-form { position: absolute; top: 1065px; left: 215px; width: 444px; height: 41px; }
  .email-field { position: absolute; left: 0; top: 0; width: 380px; height: 41px;
    border: 1px solid #cfcfcf; border-right: none; border-radius: 21px 0 0 21px;
    padding-left: 18px; font-family: "Sorts Mill Goudy", serif; font-size: 14px; line-height: 39px; color: #555; background: #fff; }
  .signup-button { position: absolute; left: 354px; top: 0; width: 90px; height: 41px;
    border-radius: 0 21px 21px 0; background: linear-gradient(#4a4a4a, var(--button));
    color: #fff; font-family: "Sorts Mill Goudy", serif; font-weight: bold; font-size: 15px; line-height: 41px; text-align: center; }
  .spam-note { position: absolute; top: 1117px; left: 0; width: 871px; text-align: center;
    font-family: "Sorts Mill Goudy", serif; font-style: italic; font-size: 11px; color: var(--muted); }

  .footer-copy { position: absolute; top: 1176px; left: 56px; font-family: "Arimo", sans-serif; font-size: 10px; color: #b0b0b0; }
  .footer-copy strong { font-weight: normal; color: #1e4f9c; margin-left: 4px; }
  .share { position: absolute; top: 1174px; left: 600px; display: flex; gap: 4px; align-items: center;
    font-family: "Arimo", sans-serif; font-size: 9px; color: #333; }
  .share-btn { border: 1px solid #c5cde0; background: #eef1f7; border-radius: 2px; padding: 1px 5px; }
  .share-count { border: 1px solid #ccc; padding: 1px 4px; background: #fff; }
  .share-gap { width: 20px; }
  .share-dot { width: 13px; height: 13px; border-radius: 2px; }
  .dot-blue { background: #3b5b98; }
  .dot-sky { background: #41a8d8; }
  .dot-grey { background: #bfc6cf; }
  .dot-steel { background: #2e75b0; }
  .dot-red { background: #e0583a; }
</style>
</head>
<body>
<div class="page">

  <svg class="swoosh" viewBox="0 0 871 160" aria-hidden="true">
    <defs>
      <linearGradient id="swoosh-green" x1="0" y1="0" x2="1" y2="0">
        <stop offset="0" stop-color="#e6f1d8" stop-opacity="0"/>
        <stop offset="0.45" stop-color="#4aa35a"/>
        <stop offset="1" stop-color="#c6e07a"/>
      </linearGradient>
      <linearGradient id="swoosh-blue" x1="0" y1="0" x2="1" y2="0">
        <stop offset="0" stop-color="#cfe6f3" stop-opacity="0"/>
        <stop offset="0.5" stop-color="#8ec6dd"/>
        <stop offset="1" stop-color="#e8f4d8"/>
      </linearGradient>
    </defs>
    <path d="M60 0 C300 18 600 50 871 140 L871 0 Z" fill="url(#swoosh-blue)" opacity="0.6"/>
    <path d="M170 0 C430 10 680 40 871 95 L871 0 Z" fill="url(#swoosh-green)"/>
  </svg>

  <h1 class="brand">Quollin</h1>
  <h2 class="tagline">Snug-Fit Wrap, Never Struggle</h2>

  <p class="intro">The Quollin Snug-Fit Wrap is an innovative quilt cover that takes the chore we all hate - changing our covers - and makes it painless.&nbsp; The Snug-Fit Wrap opens on 3 sides, and lets you dress your quilt in 60 seconds.&nbsp; It also keeps your quilt in place at all times with strategically placed velcro pieces.&nbsp; Gone are the nights where you're left with a ball of cotton at the bottom and just a thin cover at the top, and you lie sideways in a fetal position trying to get as much warmth as possible.</p>

  <h2 class="section-title">How It Works?</h2>

  <svg class="cycle" viewBox="0 440 871 490" aria-hidden="true">
    <ellipse cx="420" cy="696" rx="306" ry="243" fill="none" stroke="var(--ring)" stroke-width="1.5"/>
    <ellipse cx="432" cy="690" rx="181" ry="132" fill="var(--ring-fill)" stroke="#dcdcdc" stroke-width="1.5"/>
    <g fill="none" stroke="var(--arrow)" stroke-width="3" stroke-linecap="round">
      <path d="M292 583 Q312 568 334 560"/><path d="M326 554 L334 560 L326 566"/>
      <path d="M535 548 Q555 562 568 580"/><path d="M559 578 L568 580 L569 571"/>
      <path d="M648 706 Q645 735 630 760"/><path d="M626 751 L630 760 L639 756"/>
      <path d="M513 858 Q480 872 440 876"/><path d="M449 868 L440 876 L449 884"/>
      <path d="M232 760 Q216 738 214 705"/><path d="M207 713 L214 705 L221 712"/>
    </g>
  </svg>

  <div class="step-art open" role="img" aria-label="Illustration of the wrap opening on three sides"></div>
  <div class="step-art fasten" role="img" aria-label="Illustration of the quilt fastened inside the wrap"></div>
  <div class="step-art secure" role="img" aria-label="Illustration of the wrap closed on all sides"></div>
  <div class="step-art enjoy" role="img" aria-label="Illustration of a made bed with the wrapped quilt"></div>
  <div class="step-art attach" role="img" aria-label="Illustration of velcro pieces attached to the quilt"></div>

  <div class="step-label right label-open">The Snug-fit-wrap<br>opens on three sides</div>
  <span class="badge badge-open">2</span>
  <div class="step-label label-fasten"><span class="badge">3</span> Fasten Quilt</div>
  <div class="step-label label-secure"><span class="badge">4</span> Secure all sides</div>
  <div class="step-label label-enjoy"><span class="badge">5</span> Enjoy</div>
  <div class="step-label right label-attach">Attach Velcro<br>Pieces on Quilt</div>
  <span class="badge badge-attach">1</span>

  <div class="rule top"></div>

  <h2 class="signup-title">Be notified when we launch. <em>Sign up now!</em></h2>
  <p class="signup-note">We're giving out some free samples to some coooool mums for feedback.<br>Don't miss out this opportunity!</p>

  <form class="signup-form">
    <div class="email-field">Hannah.lowe@mailbox.com</div>
    <div class="signup-button">Sign Up!</div>
  </form>
  <p class="spam-note">We hate spams as much as you do</p>

  <div class="rule bottom"></div>

  <p class="footer-copy">All Rights Reserved - 2011 <strong>QUOLLIN</strong></p>
  <div class="share">
    <span class="share-btn">Like</span><span class="share-count">26</span>
    <span class="share-btn">Tweet</span><span class="share-count">97</span>
    <span class="share-gap"></span>
    <span class="share-dot dot-blue"></span>
    <span class="share-dot dot-sky"></span>
    <span class="share-dot dot-grey"></span>
    <span class="share-dot dot-steel"></span>
    <span class="share-dot dot-red"></span>
  </div>
</div>
</body>
</html>
```